Meadow Lantern Equine Refuge - Sponsorship Flyer

We require an A4 trifold flyer. Our colours are orange, black and white.
At The Meadow Lantern Equine Refuge, we have a number of our animals available for Sponsorship. The majority are horses or ponies reflecting our focus however from time to time other animals in need find the peace of our Sanctuary.

Your sponsorship donation helps with the cost of care for horses requiring long-term rehabilitation including ongoing vet care etc as more often than not, the horse will have arrived in poor condition.

For those horses that are unsound or aged, (but with quality of life) and therefore not suited for adoption, are allowed to live out their days here at the Sanctuary.

As a DGR* charity all donations over $2 are tax deductible.

We have two different sponsorship types…Keepers of MLER and Allies of MLER

Target Market(s)

Horse Lovers

Industry/Entity Type

Rescue

Font styles to use
Serif

Colors
EE7325
F08F49
F5BC92
FAE3D3
FDF4ED

Requirements
Must have
• KEEPERS of MLER Store/SPONSORSHIP/KEEPERS of MLER Our Guardian sponsors choose to be with us for the long term. Their regular donation helps cover the monthly costs involved with caring for our residents. We like to think of these special folk as Guardian Angels. Their generosity allows us to keep so many safe from harm in this magical place. Guardian Sponsors receive a personalised e-certificate as well as a six-monthly update. We also invite our Guardians to contact us to organise a visit to the Sanctuary at a mutually convenient time. Here, you can meet the horse or pony that has captured your heart. Sponsorship costs vary from $15 – $25 per week depending on the animal and its needs.
Should not have
• External sourced photos

```html
<!DOCTYPE html>
<html lang="en">
<head>
<meta charset="utf-8">
<title>Meadow Lantern Equine Refuge – Sponsorship Flyer</title>
<link href="https://fonts.googleapis.com/css2?family=Montserrat:wght@300;400;500;600;800;900&display=swap" rel="stylesheet">
<style>
  :root {
    --orange: #EE7325;
    --orange-light: #F08F49;
    --orange-deep: #E8502A;
    --peach: #F5BC92;
    --cream: #FDF4ED;
    --ink: #2D2D2F;
    --white: #FFFFFF;
    --stage: #BDBEC0;
    --body-grey: #3A3A3C;
  }
  * { margin: 0; padding: 0; box-sizing: border-box; }
  html, body { width: 1200px; height: 546px; overflow: hidden; background: var(--stage); }
  body { font-family: "Montserrat", Arial, sans-serif; position: relative; }

  .spread { position: absolute; top: 91px; width: 498px; height: 385px; overflow: hidden; }
  .spread--outside { left: 82px; }
  .spread--inside { left: 620px; }
  .spread__art { position: absolute; inset: 0; }

  .block { position: absolute; }
  .heading {
    font-weight: 800; line-height: 0.92;
    letter-spacing: 0.2px; color: var(--ink); font-size: 16px;
  }
  .body-copy { font-size: 6.8px; line-height: 9.4px; color: var(--body-grey); font-weight: 400; }
  .body-copy p + p { margin-top: 8px; }
  .on-dark { color: var(--white); }

  .wordmark {
    position: absolute; display: flex; align-items: center; gap: 3px;
    color: var(--white); font-weight: 600; font-size: 5.4px; line-height: 1.15;
  }
  .wordmark__square { width: 9px; height: 13px; background: var(--white); flex: none; }
  .wordmark--large { font-size: 7.4px; gap: 4px; }
  .wordmark--large .wordmark__square { width: 12px; height: 24px; }

  /* outside panels */
  .how-to { left: 21px; top: 33px; width: 132px; }
  .how-to .body-copy { margin-top: 10px; }
  .how-to .body-copy p + p { margin-top: 7px; }

  .why { left: 180px; top: 160px; width: 146px; }
  .why__title { font-size: 29px; font-weight: 900; color: var(--white); line-height: 1; }
  .why__sub { font-size: 12.6px; font-weight: 300; color: var(--white); line-height: 14px; margin-top: 1px; }
  .why .body-copy { margin-top: 18px; }

  .cover { left: 352px; top: 70px; width: 140px; text-align: center; color: var(--white); }
  .cover__line1 { font-size: 21.5px; font-weight: 900; line-height: 19px; }
  .cover__line2 { font-size: 31px; font-weight: 900; line-height: 27px; letter-spacing: 0.5px; }
  .cover__line3 { font-size: 10.2px; font-weight: 800; line-height: 12px; }
  .cover__support { font-size: 5.4px; line-height: 6.8px; margin-top: 13px; font-weight: 500; }
  .cta {
    position: absolute; left: 364px; top: 159px; width: 134px; height: 23px;
    background: var(--ink); border-radius: 12px 0 0 12px;
    color: var(--white); font-size: 6.3px; font-weight: 700; line-height: 8px;
    display: flex; align-items: center; justify-content: center; text-align: center;
  }

  /* inside panels */
  .keepers { left: 22px; top: 26px; width: 136px; }
  .keepers .body-copy { margin-top: 8px; }
  .join { left: 185px; top: 36px; width: 146px; }
  .join__sub { font-size: 10.3px; font-weight: 400; color: var(--white); margin-top: 3px; }
  .join .body-copy { margin-top: 9px; }
  .join .body-copy p + p { margin-top: 9px; }
  .allies { left: 346px; top: 72px; width: 136px; }
  .allies .body-copy { margin-top: 10px; }
</style>
</head>
<body>

<!-- Outside spread: how to sponsor / why it matters / cover -->
<section class="spread spread--outside">
  <svg class="spread__art" viewBox="0 0 498 385" width="498" height="385">
    <defs>
      <linearGradient id="coverOrange" x1="0" y1="0" x2="1" y2="1">
        <stop offset="0" stop-color="#E8502A"/>
        <stop offset="0.45" stop-color="#EE6A28"/>
        <stop offset="1" stop-color="#EF8A2C"/>
      </linearGradient>
      <linearGradient id="cornerOrange" x1="0" y1="0" x2="1" y2="1">
        <stop offset="0" stop-color="#F08F49"/>
        <stop offset="1" stop-color="#EE6A28"/>
      </linearGradient>
      <linearGradient id="grazingTones" x1="0" y1="0" x2="0" y2="1">
        <stop offset="0" stop-color="#4B5A2E"/>
        <stop offset="0.45" stop-color="#9A7A55"/>
        <stop offset="1" stop-color="#5E8A2C"/>
      </linearGradient>
      <linearGradient id="pairTones" x1="0" y1="0" x2="1" y2="1">
        <stop offset="0" stop-color="#8A5A3A"/>
        <stop offset="0.6" stop-color="#6E4A30"/>
        <stop offset="1" stop-color="#5D7A3A"/>
      </linearGradient>
    </defs>
    <rect x="0" y="0" width="166" height="385" fill="var(--white)"/>
    <rect x="166" y="0" width="332" height="385" fill="var(--ink)"/>
    <g role="img" aria-label="Photo of two brown horses nuzzling in a paddock">
      <path d="M0 195 Q60 188 92 214 Q140 268 166 385 H0 Z" fill="url(#pairTones)"/>
    </g>
    <path d="M0 290 Q112 298 166 385 H0 Z" fill="url(#cornerOrange)"/>
    <g role="img" aria-label="Photo of two shaggy ponies grazing on green grass">
      <rect x="333" y="170" width="165" height="215" fill="url(#grazingTones)"/>
    </g>
    <path d="M172 0 C190 112 330 215 498 205 V0 Z" fill="url(#coverOrange)"/>
    <path d="M333 0 H498 V205 C440 210 385 203 333 190 Z" fill="#EF852C" opacity="0.55"/>
  </svg>

  <div class="block how-to">
    <h2 class="heading">HOW TO<br>SPONSOR</h2>
    <div class="body-copy">
      <p>It’s easy to become a Guardian or Friend of MLER:</p>
      <p>1. Visit our website or scan the QR code<br>2. Choose your sponsorship type and amount<br>3. Start making a difference today!</p>
      <p>Every dollar helps us give these animals the second chance they deserve.</p>
    </div>
  </div>
  <div class="wordmark" style="left:21px; top:352px;">
    <span>Meadow Lantern<br>Equine Refuge</span><span class="wordmark__square"></span>
  </div>

  <div class="block why">
    <h2 class="why__title">Why</h2>
    <p class="why__sub">Sponsorship<br>Matters</p>
    <div class="body-copy on-dark">
      <p>At The Meadow Lantern Equine Refuge, we provide a safe and loving home for rescued horses and ponies. Many arrive in poor condition, requiring long-term rehabilitation and vet care. Some will never be adopted due to age or injury, but they still deserve love, peace, and dignity.</p>
      <p>Your sponsorship helps cover daily costs such as feed, medical treatments, and care — ensuring these animals can live out their lives in safety and comfort.</p>
    </div>
  </div>

  <div class="wordmark wordmark--large" style="left:383px; top:30px;">
    <span>Meadow Lantern<br>Equine Refuge</span><span class="wordmark__square"></span>
  </div>
  <div class="block cover">
    <p class="cover__line1">SPONSOR</p>
    <p class="cover__line2">A LIFE</p>
    <p class="cover__line3">MAKE A DIFFERENCE</p>
    <p class="cover__support">Support horses and ponies at The Meadow<br>Lantern Equine Refuge</p>
  </div>
  <div class="cta">Become a Guardian<br>or Friend of MLER today!</div>
</section>

<!-- Inside spread: keepers / join us / allies -->
<section class="spread spread--inside">
  <svg class="spread__art" viewBox="0 0 498 385" width="498" height="385">
    <defs>
      <linearGradient id="ponyFade" x1="0" y1="0" x2="0" y2="1">
        <stop offset="0" stop-color="#FFFFFF"/>
        <stop offset="0.35" stop-color="#E9DCCF"/>
        <stop offset="1" stop-color="#B89478"/>
      </linearGradient>
      <linearGradient id="herdTones" x1="0" y1="0" x2="1" y2="1">
        <stop offset="0" stop-color="#8C6A44"/>
        <stop offset="0.5" stop-color="#6B3F28"/>
        <stop offset="1" stop-color="#3E3330"/>
      </linearGradient>
      <linearGradient id="bandOrange" x1="0" y1="1" x2="1" y2="0">
        <stop offset="0" stop-color="#EE7325" stop-opacity="0"/>
        <stop offset="0.5" stop-color="#EE7325" stop-opacity="0.8"/>
        <stop offset="1" stop-color="#E8502A"/>
      </linearGradient>
    </defs>
    <rect x="0" y="0" width="166" height="385" fill="var(--white)"/>
    <g role="img" aria-label="Photo of a palomino pony with a pale mane standing by a fence">
      <rect x="0" y="228" width="166" height="157" fill="url(#ponyFade)"/>
    </g>
    <rect x="166" y="0" width="166" height="385" fill="var(--ink)"/>
    <rect x="332" y="0" width="166" height="385" fill="var(--white)"/>
    <path d="M367 0 Q420 34 498 41 V0 Z" fill="var(--orange)"/>
    <path d="M178 385 Q280 226 498 213 V222 Q292 248 193 385 Z" fill="url(#bandOrange)"/>
    <g role="img" aria-label="Photo of a herd of horses running across a grassy field">
      <path d="M193 385 Q292 248 498 222 V385 Z" fill="url(#herdTones)"/>
    </g>
  </svg>

  <div class="block keepers">
    <h2 class="heading">KEEPERS<br>of MLER</h2>
    <div class="body-copy">
      <p>Our Guardian sponsors choose to be with us for the long term. Their regular donation helps cover the monthly costs of caring for our residents. We like to think of these special folk as Guardian Angels.</p>
      <p>Their generosity allows us to keep so many safe from harm in this magical place.</p>
      <p>Guardian Sponsors receive a personalised e-certificate and a six-monthly update. We also invite our Guardians to organise a visit to meet the horse or pony that has captured their heart.</p>
      <p>Sponsorship ranges from $15–$25 per week, depending on the animal’s needs.</p>
    </div>
  </div>

  <div class="block join">
    <h2 class="heading on-dark">JOIN US</h2>
    <p class="join__sub">in Making a Difference</p>
    <div class="body-copy on-dark">
      <p>As a registered DGR charity, all donations over $2 are tax deductible.</p>
      <p>Contact Us:<br>The Meadow Lantern Equine Refuge</p>
      <p>Phone:<br>Email:<br>Website:</p>
      <p>Follow us on social media:<br>[Icon Sharebook, Picturegram]</p>
    </div>
  </div>

  <div class="block allies">
    <h2 class="heading">ALLIES<br>of MLER</h2>
    <div class="body-copy">
      <p>Allies of MLER support the Sanctuary with a flexible, heartfelt donation. This sponsorship is ideal for those who want to contribute but may not be able to commit long-term.</p>
      <p>Allies receive a digital thank-you note and occasional updates about our work and residents.</p>
    </div>
  </div>
  <div class="wordmark" style="left:424px; top:344px;">
    <span>Meadow Lantern<br>Equine Refuge</span><span class="wordmark__square"></span>
  </div>
</section>

</body>
</html>
```